Creative Businesss Card desgin!

Create a business card for our business Gleam window cleaning!
We are open to creative ideas as long as it maintains a professional image.

Target Market(s)

Small Commercial window cleaning clients including car dealerships, strata manager, cafe

Industry/Entity Type

Window Cleaning

Contact Information for Business Card

Daniel Prescott
General Manager
Gleam Window Cleaning

daniel@gleamservices.com.au
pane-care-southbank.com.au
Ph: 1800 GET GLEAM
Mob: 0437 582 061

Colors
fbed22
0392cd

Requirements
Should not have
• Stock window cleaning/ squeegee graphics

```html
<!DOCTYPE html>
<html lang="en">
<head>
<meta charset="utf-8">
<title>Gleam Window Cleaning — Business Card</title>
<link href="https://fonts.googleapis.com/css2?family=Ubuntu:wght@500;700&display=swap" rel="stylesheet">
<style>
  :root {
    --page-bg: #f2f2f2;
    --sky: #33b2f2;
    --sky-light: #4cc3f7;
    --sky-deep: #2aa5e8;
    --gleam-yellow: #eef21c;
    --band-yellow: #f1d81a;
    --navy: #0d3a78;
    --royal: #1a4aa8;
    --card-white: #ffffff;
  }
  * { box-sizing: border-box; margin: 0; padding: 0; }
  html, body {
    width: 1200px;
    height: 1200px;
    overflow: hidden;
    background: var(--page-bg);
    font-family: "Ubuntu", Arial, sans-serif;
  }
  .canvas { position: relative; width: 1200px; height: 1200px; }

  .card {
    position: absolute;
    width: 612px;
    height: 350px;
    overflow: hidden;
  }

  /* ---------- Front face ---------- */
  .card-front {
    left: 272px;
    top: 178px;
    background: linear-gradient(135deg, var(--sky-deep) 0%, var(--sky) 45%, var(--sky-light) 75%, var(--sky) 100%);
  }
  .card-front .base-band {
    position: absolute;
    left: 0; top: 0;
    width: 612px; height: 350px;
  }
  .wordmark {
    color: var(--gleam-yellow);
    font-weight: 700;
    line-height: 1;
    text-transform: uppercase;
  }
  .card-front .wordmark {
    position: absolute;
    left: 165px;
    top: 118px;
    width: 270px;
    text-align: center;
  }
  .card-front .wordmark-name { display: block; font-size: 72px; letter-spacing: 2px; }
  .card-front .wordmark-tag { display: block; font-size: 22px; margin-top: 8px; letter-spacing: 0.5px; }

  /* ---------- Back face ---------- */
  .card-back {
    left: 287px;
    top: 626px;
    background: var(--card-white);
  }
  .card-back .side-strip {
    position: absolute;
    left: 0; top: 0;
    width: 33px; height: 350px;
    background: var(--sky);
  }
  .card-back .brand-panel {
    position: absolute;
    left: 0; top: 0;
    width: 612px; height: 350px;
  }
  .card-back .wordmark {
    position: absolute;
    right: 12px;
    top: 20px;
    text-align: center;
  }
  .card-back .wordmark-name { display: block; font-size: 43px; letter-spacing: 1px; }
  .card-back .wordmark-tag { display: block; font-size: 15px; margin-top: 4px; }

  .holder {
    position: absolute;
    left: 45px;
    top: 14px;
  }
  .holder-name {
    font-size: 31px;
    font-weight: 700;
    color: var(--navy);
    letter-spacing: 0.3px;
  }
  .holder-title {
    font-size: 20px;
    font-weight: 700;
    color: var(--royal);
    margin-top: 2px;
  }

  .contacts {
    position: absolute;
    left: 12px;
    top: 228px;
    list-style: none;
  }
  .contacts li {
    display: flex;
    align-items: center;
    height: 27.5px;
    font-size: 19px;
    font-weight: 500;
    color: var(--navy);
  }
  .contacts .icon {
    width: 18px;
    height: 18px;
    margin-right: 8px;
    flex: none;
  }
</style>
</head>
<body>
<main class="canvas">

  <!-- Front face -->
  <section class="card card-front" aria-label="Business card front">
    <svg class="base-band" viewBox="0 0 612 350" aria-hidden="true">
      <defs>
        <filter id="band-glow" x="-20%" y="-200%" width="140%" height="500%">
          <feGaussianBlur stdDeviation="8"/>
        </filter>
      </defs>
      <polygon points="360,300 612,268 612,290 380,312" fill="#fbf36a" opacity="0.7" filter="url(#band-glow)"/>
      <polygon points="0,310 612,262 612,350 0,350" fill="var(--card-white)"/>
      <polygon points="0,308 612,258 612,268 0,318" fill="var(--band-yellow)"/>
    </svg>
    <div class="wordmark">
      <span class="wordmark-name">Gleam</span>
      <span class="wordmark-tag">Window Cleaning</span>
    </div>
  </section>

  <!-- Back face -->
  <section class="card card-back" aria-label="Business card back">
    <div class="side-strip"></div>
    <svg class="brand-panel" viewBox="0 0 612 350" aria-hidden="true">
      <defs>
        <filter id="edge-glow" x="-100%" y="-10%" width="300%" height="120%">
          <feGaussianBlur stdDeviation="7"/>
        </filter>
      </defs>
      <polygon points="384,0 398,0 424,350 410,350" fill="#f6f37a" opacity="0.8" filter="url(#edge-glow)"/>
      <polygon points="396,0 612,0 612,350 420,350" fill="var(--sky)"/>
      <polygon points="384,0 398,0 422,350 408,350" fill="var(--gleam-yellow)"/>
    </svg>
    <div class="wordmark">
      <span class="wordmark-name">Gleam</span>
      <span class="wordmark-tag">Window Cleaning</span>
    </div>

    <div class="holder">
      <h1 class="holder-name">Daniel Prescott</h1>
      <p class="holder-title">General Manager</p>
    </div>

    <ul class="contacts">
      <li>
        <svg class="icon" viewBox="0 0 20 20" aria-hidden="true">
          <circle cx="10" cy="10" r="3.6" fill="none" stroke="var(--band-yellow)" stroke-width="2"/>
          <path d="M13.6 7v4.2c0 1.6 2.8 1.8 2.8-1.2A6.4 6.4 0 1 0 12.5 16" fill="none" stroke="var(--band-yellow)" stroke-width="2" stroke-linecap="round"/>
        </svg>
        daniel@gleamservices.com.au
      </li>
      <li>
        <svg class="icon" viewBox="0 0 20 20" aria-hidden="true">
          <circle cx="10" cy="10" r="7.5" fill="none" stroke="var(--band-yellow)" stroke-width="1.8"/>
          <ellipse cx="10" cy="10" rx="3.2" ry="7.5" fill="none" stroke="var(--band-yellow)" stroke-width="1.5"/>
          <line x1="2.5" y1="10" x2="17.5" y2="10" stroke="var(--band-yellow)" stroke-width="1.5"/>
        </svg>
        pane-care-southbank.com.au
      </li>
      <li>
        <svg class="icon" viewBox="0 0 20 20" aria-hidden="true">
          <path d="M5 3l3 3.2-1.6 2.2a9 9 0 0 0 4.6 4.6l2.2-1.6L16.4 14.6 14.4 17C8 16.4 3.6 12 3 5.6z" fill="var(--band-yellow)"/>
        </svg>
        Ph: 1800 GET GLEAM
      </li>
      <li>
        <svg class="icon" viewBox="0 0 20 20" aria-hidden="true">
          <path d="M5 3l3 3.2-1.6 2.2a9 9 0 0 0 4.6 4.6l2.2-1.6L16.4 14.6 14.4 17C8 16.4 3.6 12 3 5.6z" fill="var(--band-yellow)"/>
        </svg>
        Mob: 0437 582 061
      </li>
    </ul>
  </section>

</main>
</body>
</html>
```